Support People to improve their image and well-being by provided personalised advise

We need a design for business cards that could be used for production on plato press. We build a new business in our region for advising mostly women (also men though) on style embracing several aspects including fashion, style, self-confidence and ultimately your internal and external image. The business card should be "classy", "french-style". The business is located in the french -speaking part of Switzerland, close to France. The name of the company is Velo Grace

Target Market(s)

Service fees won't be cheap (medium to premium) thus we target mid-class to upper-class women (1st target) and men (2nd target)

Industry/Entity Type

Life Coaching

Contact Information for Business Card

Conseil en Image

+41 79 418 62 07
morinetu@velo-grace.ch
linkedin.com/in/tu-moro-netia

Logo Text

Velo Grace

Colors

Designer to choose colors to be used in the design.

```html
<!DOCTYPE html>
<html lang="fr">
<head>
<meta charset="utf-8">
<title>Velo Grace — Cartes de visite</title>
<link rel="stylesheet" href="https://fonts.googleapis.com/css2?family=Roboto+Condensed:wght@400;700&display=swap">
<style>
  :root {
    --backdrop: #ecebe8;
    --dark-edge: #1b1b1c;
    --dark-core: #5b5b5d;
    --light-ink: #f2f2f2;
    --paper: #ffffff;
    --paper-band: #ededed;
    --ink: #6a6a6a;
    --ink-strong: #555555;
    --rule: #9a9a9a;
  }
  * { margin: 0; padding: 0; box-sizing: border-box; }
  html, body {
    width: 1200px; height: 801px; overflow: hidden;
    background: var(--backdrop);
    font-family: "Roboto Condensed", "Arial Narrow", sans-serif;
  }
  .stage {
    position: relative; width: 1200px; height: 801px;
    display: flex; align-items: center; justify-content: center; gap: 40px;
  }
  .card {
    position: relative; width: 540px; height: 309px;
    border-radius: 3px;
    box-shadow: 0 8px 24px rgba(0,0,0,.18);
    overflow: hidden;
  }
  /* Front */
  .card--front {
    background: radial-gradient(ellipse 60% 70% at 55% 60%, var(--dark-core), var(--dark-edge));
    color: var(--light-ink);
  }
  .front-brand {
    position: absolute; left: 0; right: 0; top: 112px;
    display: flex; align-items: center; justify-content: center; gap: 14px;
  }
  .brand-dot {
    width: 44px; height: 44px; border-radius: 50%;
    border: 3px solid currentColor; flex: none;
  }
  .front-name { font-weight: 700; font-size: 38px; letter-spacing: .5px; }
  .front-tagline {
    position: absolute; left: 0; right: 0; top: 222px; text-align: center;
    font-weight: 700; font-size: 17px; letter-spacing: .5px;
  }
  /* Back */
  .card--back { background: var(--paper); color: var(--ink); }
  .edge-band { position: absolute; left: 0; right: 0; height: 12px; background: var(--paper-band); }
  .edge-band--top { top: 0; }
  .edge-band--bottom { bottom: 0; }
  .back-brand {
    position: absolute; left: 0; width: 270px; top: 0; bottom: 0;
    display: flex; flex-direction: column; align-items: center; justify-content: center;
  }
  .back-brand .brand-dot { width: 52px; height: 52px; color: var(--ink); margin-bottom: 12px; }
  .back-name { font-weight: 700; font-size: 32px; color: var(--ink); line-height: 1; }
  .back-tagline { font-weight: 700; font-size: 11px; letter-spacing: .4px; color: var(--ink); margin-top: 3px; }
  .divider {
    position: absolute; left: 276px; top: 40px; bottom: 40px;
    width: 1px; background: var(--rule);
  }
  .contact {
    position: absolute; left: 300px; top: 118px;
    list-style: none; font-size: 14px; line-height: 20px; color: var(--ink-strong);
  }
</style>
</head>
<body>
<main class="stage">
  <section class="card card--front" aria-label="Recto de la carte">
    <div class="front-brand">
      <span class="brand-dot"></span>
      <span class="front-name">VELO GRACE</span>
    </div>
    <p class="front-tagline">CONSEIL EN IMAGE</p>
  </section>

  <section class="card card--back" aria-label="Verso de la carte">
    <div class="edge-band edge-band--top"></div>
    <div class="edge-band edge-band--bottom"></div>
    <div class="back-brand">
      <span class="brand-dot"></span>
      <span class="back-name">VELO GRACE</span>
      <span class="back-tagline">CONSEIL EN IMAGE</span>
    </div>
    <div class="divider"></div>
    <ul class="contact">
      <li>+41 79 418 62 07</li>
      <li>morinetu@velo-grace.ch</li>
      <li>linkedin.com/in/tu-moro-netia</li>
    </ul>
  </section>
</main>
</body>
</html>
```